FB and Youtube banner design for HVAC company

I would like an appealing site page banner for business page on Facebook (851w x 315h pixels) and one for youtube (2560w x 1440h pixels) for hvac company. Business card design and logo are attached. Company name is Bright Meadow Air Conditioning, Refrigeration, and Heating.

NOTE: I put the business cards and log up to see some of the artwork the company is using. It's not to replicate that in the banner images.

Target Market(s)

Interested business and homeowner visitors to Facebook business page and youtube channel page.

Industry/Entity Type

Hvac

Font styles to use
Sans Serif

Requirements
Must have
• See logo for color scheme.
Should not have
• This should not look like a business card. Think of what is typically the banner on a facebook business page and youtube channel.

```html
<!DOCTYPE html>
<html lang="en">
<head>
<meta charset="utf-8">
<title>Bright Meadow – Service Banner</title>
<link rel="stylesheet" href="https://fonts.googleapis.com/css2?family=Roboto+Condensed:wght@400;700&display=swap">
<style>
  :root{
    --blue-deep:#1a2f9e;
    --blue-mid:#2f4fd0;
    --blue-light:#5a7cf0;
    --orange:#f26a1b;
    --white:#ffffff;
    --ink:#1b1f3a;
    --brand-blue:#2343c4;
    --product-a:#c9ced6;
    --product-b:#6b7280;
  }
  *{margin:0;padding:0;box-sizing:border-box}
  html,body{width:1200px;height:457px;overflow:hidden;background:var(--white)}
  .banner{
    position:relative;width:1200px;height:457px;overflow:hidden;
    background:radial-gradient(ellipse 70% 90% at 30% 40%, var(--blue-light) 0%, var(--blue-mid) 45%, var(--blue-deep) 100%);
    font-family:"Roboto Condensed", "Arial Narrow", sans-serif;
    color:var(--white);
  }
  .wave{position:absolute;inset:0;width:1200px;height:457px}
  .headline{
    position:absolute;left:170px;top:50px;width:260px;
    text-align:center;font-weight:700;font-size:24px;line-height:1.3;letter-spacing:.3px;
    text-transform:uppercase;
  }
  .products{
    position:absolute;left:85px;top:118px;width:540px;height:339px;
    border-radius:6px 6px 0 0;
    background:linear-gradient(160deg, var(--product-a) 0%, #9aa2ae 55%, var(--product-b) 100%);
  }
  .services{
    position:absolute;left:788px;top:34px;list-style:none;
  }
  .services li{
    display:flex;align-items:center;gap:14px;
    font-weight:700;font-size:22px;text-transform:uppercase;height:49px;letter-spacing:.3px;
  }
  .services svg{width:26px;height:30px;flex:none}
  .scope{
    position:absolute;left:722px;top:190px;
    font-weight:700;font-size:23px;line-height:1.4;text-transform:uppercase;letter-spacing:.2px;
  }
  .brand{
    position:absolute;left:816px;top:316px;display:flex;align-items:center;gap:12px;
  }
  .brand-dot{width:74px;height:74px;border-radius:50%;background:var(--orange);flex:none}
  .brand-name{
    font-weight:700;font-size:40px;line-height:1;color:var(--brand-blue);text-transform:uppercase;
  }
  .brand-tagline{
    position:absolute;left:816px;top:400px;
    font-weight:700;font-size:11.5px;letter-spacing:1.2px;color:var(--ink);text-transform:uppercase;
  }
</style>
</head>
<body>
<div class="banner">
  <svg class="wave" viewBox="0 0 1200 457" aria-hidden="true">
    <path d="M0 412 C 420 400, 820 330, 1200 230 L1200 457 L0 457 Z" fill="var(--orange)"/>
    <path d="M0 430 C 430 418, 830 352, 1200 252 L1200 457 L0 457 Z" fill="var(--white)"/>
  </svg>

  <h1 class="headline">Service you can count on.<br>Like clockwork.</h1>

  <div class="products" role="img" aria-label="Photo of commercial equipment: an ice machine, a drinks vending machine and a soft-serve ice cream machine"></div>

  <ul class="services">
    <li><svg viewBox="0 0 26 30" aria-hidden="true"><rect x="1" y="9" width="18" height="18" rx="2" fill="var(--white)"/><path d="M5 16 L10 22 L24 2" fill="none" stroke="var(--orange)" stroke-width="4" stroke-linecap="round" stroke-linejoin="round"/></svg>Installation</li>
    <li><svg viewBox="0 0 26 30" aria-hidden="true"><rect x="1" y="9" width="18" height="18" rx="2" fill="var(--white)"/><path d="M5 16 L10 22 L24 2" fill="none" stroke="var(--orange)" stroke-width="4" stroke-linecap="round" stroke-linejoin="round"/></svg>Maintenance</li>
    <li><svg viewBox="0 0 26 30" aria-hidden="true"><rect x="1" y="9" width="18" height="18" rx="2" fill="var(--white)"/><path d="M5 16 L10 22 L24 2" fill="none" stroke="var(--orange)" stroke-width="4" stroke-linecap="round" stroke-linejoin="round"/></svg>Service &amp; Repair</li>
  </ul>

  <p class="scope">On air conditioning, refrigeration<br>&amp; heating units.</p>

  <div class="brand">
    <span class="brand-dot" aria-hidden="true"></span>
    <span class="brand-name">Bright<br>Meadow</span>
  </div>
  <p class="brand-tagline">Air Conditioning • Refrigeration • Heating</p>
</div>
</body>
</html>
```